Wendle Pay Track Quick View Page

Make it look more attractive -- this is the first page customers see after they sign up.
We just recreated the account setup page -- I send this in to give you a reference for colors and design.

```html
<!DOCTYPE html>
<html lang="en">
<head>
<meta charset="utf-8">
<title>Wendle Pay Track – Quick View</title>
<link href="https://fonts.googleapis.com/css2?family=Montserrat:ital,wght@0,400;0,500;0,600;0,700;0,800;1,500&display=swap" rel="stylesheet">
<style>
:root{
  --blue:#1c22d8;
  --blue-deep:#0b0fb5;
  --navy:#0a0f9e;
  --green:#1ec872;
  --ink:#1d1d22;
  --muted:#555a66;
  --white:#ffffff;
  --row-grey:#eceef1;
  --row-green:#d8f1dc;
  --row-yellow:#fbf5dd;
  --row-pink:#f1dada;
  --row-blue:#d6e8f5;
  --tab-grey:#e9eaed;
  --placeholder:#e3e6ee;
}
*{box-sizing:border-box;margin:0;padding:0}
html,body{width:1200px;height:2931px;overflow:hidden}
body{position:relative;font-family:"Montserrat",sans-serif;color:var(--ink);background:var(--white)}
.abs{position:absolute}
.header-bg{left:0;top:0}
.brand{display:flex;align-items:center;gap:14px;color:var(--white);font-weight:500;font-size:30px}
.brand-square{width:70px;height:60px;border-radius:6px;background:var(--white)}
.site-brand{left:145px;top:50px}
.topbar{right:145px;top:12px;display:flex;align-items:center;gap:22px}
.topbar-phone{color:var(--white);font-weight:700;font-size:21px;display:flex;align-items:center;gap:8px}
.login-btn{background:var(--green);color:var(--white);font-weight:700;font-size:17px;padding:13px 28px;border-radius:26px}
.main-nav{right:145px;top:78px;display:flex;gap:34px;font-weight:700;font-size:17px;color:var(--white)}
.video{left:226px;top:195px;width:750px;height:407px;border-radius:16px;background:linear-gradient(135deg,#eef0f0,#dcdfe0);overflow:hidden}
.play{position:absolute;left:331px;top:160px;width:86px;height:86px;border-radius:50%;background:#e0443c}
.play svg{position:absolute;left:30px;top:24px}
.feature{top:680px;width:270px;text-align:center}
.feature-icon{width:86px;height:86px;margin:0 auto;border-radius:50%;background:var(--placeholder)}
.feature h3{margin-top:40px;font-size:22px;font-weight:700;line-height:27px}
.feature p{margin:16px auto 0;max-width:245px;font-size:14px;color:var(--muted);line-height:22.5px}
.note{left:0;width:1200px;top:958px;text-align:center;font-style:italic;font-weight:500;font-size:16px;color:var(--navy)}
.next-btn{left:413px;top:1030px;width:375px;height:80px;border-radius:40px;background:var(--green);color:var(--white);font-weight:700;font-size:19px;display:flex;align-items:center;justify-content:center}
.welcome{left:0;width:1200px;top:1205px;text-align:center;font-size:41px;font-weight:800;color:var(--navy)}
.welcome span{color:var(--green)}
.intro{left:200px;width:800px;top:1283px;text-align:center;font-size:14px;line-height:22.5px;color:var(--muted)}
.card-shadow{left:140px;top:1448px;width:920px;height:490px;background:var(--green);border-radius:14px;transform:rotate(1.4deg)}
.card{left:144px;top:1458px;width:912px;height:484px;background:var(--white);border-radius:14px;box-shadow:0 4px 16px rgba(0,0,0,.08)}
.card h2{position:absolute;left:0;width:100%;top:70px;text-align:center;font-size:24px;font-weight:700}
.stats{position:absolute;left:62px;top:136px;display:grid;grid-template-columns:387px 387px;column-gap:14px;row-gap:5px}
.stat{height:51px;display:flex;align-items:center;padding:0 24px;font-size:15px;color:#3a3d46}
.stat .label{width:290px;line-height:18px}
.stat.right .label{width:276px}
.stat .value{font-weight:800;color:var(--navy)}
.r-grey{background:var(--row-grey)}.r-green{background:var(--row-green)}.r-yellow{background:var(--row-yellow)}.r-pink{background:var(--row-pink)}.r-blue{background:var(--row-blue)}
.tabs{left:142px;top:2024px;display:flex;gap:4px}
.tab{width:303px;height:44px;display:flex;align-items:center;justify-content:center;font-weight:700;font-size:16px;background:var(--tab-grey);color:var(--ink)}
.tab.active{background:var(--blue-deep);color:var(--white)}
.start-title{left:140px;top:2113px;font-size:33px;font-weight:700}
.field{height:52px;border:1px solid #b9bcc4;display:flex;align-items:center;padding:0 14px 0 30px;font-size:14.5px;color:#444}
.field .label{flex:1}
.apply-btn{background:var(--green);color:var(--white);font-weight:700;font-size:14px;padding:11px 16px}
.create-btn{left:141px;top:2333px;width:246px;height:54px;border-radius:27px;background:var(--green);color:var(--white);font-weight:700;font-size:13px;display:flex;align-items:center;justify-content:center}
.footer-bg{left:0;top:2385px}
.footer-brand{left:0;width:1200px;top:2590px;justify-content:center}
.footer-contact{left:0;width:1200px;top:2694px;display:flex;justify-content:center;align-items:center;gap:14px;color:var(--white);font-weight:700;font-size:20px}
.footer-nav{left:0;width:1200px;top:2758px;display:flex;justify-content:center;gap:34px;color:var(--white);font-weight:700;font-size:17px}
.copyright{left:0;width:1200px;top:2810px;text-align:center;color:var(--white);font-size:13px}
.social{left:0;width:1200px;top:2862px;display:flex;justify-content:center;gap:18px}
.social span{width:26px;height:26px;border-radius:50%;background:var(--white)}
</style>
</head>
<body>

<svg class="abs header-bg" width="1200" height="540" viewBox="0 0 1200 540" aria-hidden="true">
  <defs><linearGradient id="hg" x1="0" y1="0" x2="1" y2="1"><stop offset="0" stop-color="#2a33ea"/><stop offset="1" stop-color="#1418c0"/></linearGradient></defs>
  <path d="M0 0H1200V462C900 440 300 470 0 530Z" fill="url(#hg)"/>
  <path d="M0 530C300 480 700 455 1200 462V532C900 490 500 500 0 530Z" fill="var(--green)"/>
</svg>

<div class="abs brand site-brand"><span class="brand-square"></span>Wendle Pay Track</div>
<div class="abs topbar">
  <span class="topbar-phone"><svg width="18" height="18" viewBox="0 0 24 24"><path fill="#1ec872" d="M6.6 10.8a15 15 0 0 0 6.6 6.6l2.2-2.2a1 1 0 0 1 1-.25 11 11 0 0 0 3.6.6 1 1 0 0 1 1 1V20a1 1 0 0 1-1 1A17 17 0 0 1 3 4a1 1 0 0 1 1-1h3.5a1 1 0 0 1 1 1c0 1.25.2 2.45.6 3.6a1 1 0 0 1-.25 1z"/></svg>(555) 210-4873</span>
  <span class="login-btn">LOGIN</span>
</div>
<nav class="abs main-nav"><span>Home</span><span>Testimonials</span><span>Max Scores</span><span>FAQ</span><span>Blog</span></nav>

<div class="abs video" role="img" aria-label="Explainer video illustration: a puzzled man and a helpful advisor beside a laptop showing a credit score">
  <div class="play"><svg width="32" height="38" viewBox="0 0 32 38"><path d="M0 0L32 19L0 38Z" fill="#fff"/></svg></div>
</div>

<div class="abs feature" style="left:134px"><div class="feature-icon"></div><h3>See What Lenders see</h3><p>Same credit report and 3 ScoreLine score lenders use and access WPT's Proprietary technology</p></div>
<div class="abs feature" style="left:465px"><div class="feature-icon"></div><h3>Know that lenders know</h3><p>Potential mortgage and auto loan qualification</p></div>
<div class="abs feature" style="left:795px"><div class="feature-icon"></div><h3>Know what you can do</h3><p>Discover your step-by-step solution to higher ScoreLine Scores</p></div>

<p class="abs note">*81 Average Point Improvement Using WPT's Proprietary technology</p>
<div class="abs next-btn">NEXT : ANALYZER REPORT &nbsp;&gt;&gt;</div>

<h1 class="abs welcome">Welome to <span>Wendle Pay</span> Track</h1>
<p class="abs intro">Quick View provides a summary of Wendle Pay Track's analysis from your most recent 3-bureau credit report and ScoreLine® scores. Each section gives a preview of your Analyzer, Planner and Qualifier. The Personal Planner offers solutions in your credit report to increase your ScoreLine credit scores. For the entire report, you may click "Programs" on the menu bar and select each program for your review. Let's get on the road to higher ScoreLine credit scores!</p>

<div class="abs card-shadow"></div>
<section class="abs card">
  <h2>Here is a quick overview of what we found in your credit report</h2>
  <div class="stats">
    <div class="stat r-grey"><span class="label">Number of Accounts</span><span class="value">5</span></div>
    <div class="stat right r-grey"><span class="label">Total past due amount</span><span class="value">$5,887.00</span></div>
    <div class="stat r-green"><span class="label"># of Credit Cards with a balance</span><span class="value">2</span></div>
    <div class="stat right r-green"><span class="label"># Of account with a balance</span><span class="value">7</span></div>
    <div class="stat r-yellow"><span class="label"># of accounts with a late payment</span><span class="value">4</span></div>
    <div class="stat right r-yellow"><span class="label">Total credit card balannce</span><span class="value">$139.00</span></div>
    <div class="stat r-pink"><span class="label"># of Openaccounts</span><span class="value">2</span></div>
    <div class="stat right r-pink"><span class="label"># Of collections</span><span class="value">8</span></div>
    <div class="stat r-blue"><span class="label">Highest credit card balance</span><span class="value">$92.00</span></div>
    <div class="stat right r-blue"><span class="label"># Of public records, banruptcies, judgements and tax liens</span><span class="value">0</span></div>
  </div>
</section>

<div class="abs tabs"><div class="tab active">CREATE ACCOUNT</div><div class="tab">CREATE ACCOUNT</div><div class="tab">CREATE ACCOUNT</div></div>
<h2 class="abs start-title">Let’s Get Started</h2>
<div class="abs field" style="left:141px;top:2186px;width:381px"><span class="label">Email Address</span><svg width="14" height="11" viewBox="0 0 14 11"><rect width="14" height="11" rx="1" fill="#222"/><path d="M0 1L7 6L14 1" stroke="#fff" fill="none" stroke-width="1.3"/></svg></div>
<div class="abs field" style="left:533px;top:2186px;width:445px;padding-right:6px"><span class="label">Promotional Code (Optional)</span><span class="apply-btn">APPLY</span></div>
<div class="abs field" style="left:141px;top:2255px;width:381px"><span class="label">Password</span><svg width="12" height="14" viewBox="0 0 12 14"><path d="M3 6V4a3 3 0 0 1 6 0v2" stroke="#222" stroke-width="1.8" fill="none"/><rect y="6" width="12" height="8" rx="1" fill="#222"/></svg></div>
<div class="abs create-btn">CREATE YOUR ACCOUNT</div>

<svg class="abs footer-bg" width="1200" height="546" viewBox="0 0 1200 546" aria-hidden="true">
  <path d="M0 0L472 120L1200 0V546H0Z" fill="var(--green)"/>
  <path d="M0 10L472 150L1200 10V546H0Z" fill="var(--blue-deep)"/>
</svg>
<div class="abs brand footer-brand"><span class="brand-square"></span>Wendle Pay Track</div>
<div class="abs footer-contact">
  <svg width="16" height="20" viewBox="0 0 16 20"><path d="M8 0a8 8 0 0 1 8 8c0 6-8 12-8 12S0 14 0 8a8 8 0 0 1 8-8z" fill="#fff"/><circle cx="8" cy="8" r="3" fill="#0b0fb5"/></svg>
  <span>418 Harbor Lane, Suite 210, Millbrook, Oregon 97311</span><span>|</span>
  <svg width="18" height="18" viewBox="0 0 24 24"><path fill="#fff" d="M6.6 10.8a15 15 0 0 0 6.6 6.6l2.2-2.2a1 1 0 0 1 1-.25 11 11 0 0 0 3.6.6 1 1 0 0 1 1 1V20a1 1 0 0 1-1 1A17 17 0 0 1 3 4a1 1 0 0 1 1-1h3.5a1 1 0 0 1 1 1c0 1.25.2 2.45.6 3.6a1 1 0 0 1-.25 1z"/></svg>
  <span>(555) 210-4873</span>
</div>
<nav class="abs footer-nav"><span>HOME</span><span>TESTIMONIALS</span><span>MAX SCORES</span><span>FAQ</span><span>BLOG</span></nav>
<p class="abs copyright">Copyright 2022 by Wendle Pay Track.All Rights Reserved &nbsp;|&nbsp; Privacy</p>
<div class="abs social" aria-label="Social media links"><span></span><span></span><span></span></div>

</body>
</html>
```